Halvorn spray foam and Environmental

I have business cards but need new ones. The ones I have are very bland. Here is. Y company website http://www.halvornsprayfoam.ca

Also I can send you copies of the current cards
I would also need my current logo on the new design as well.. Also spray foam and Environmental

Industry/Entity Type

Business

Logo Text

Halvorn.

```html
<!DOCTYPE html>
<html lang="en">
<head>
<meta charset="utf-8">
<title>Halvorn Spray Foam and Environmental – Business Cards</title>
<link href="https://fonts.googleapis.com/css2?family=Montserrat:wght@600;700&family=Work+Sans:wght@400;500&display=swap" rel="stylesheet">
<style>
  :root {
    --purple: #5b2a7c;
    --ink: #3c3e48;
    --grey-band: #b9bcbb;
    --card: #ffffff;
    --backdrop: #2f2f31;
    --text: #3f3f44;
  }
  * { box-sizing: border-box; margin: 0; padding: 0; }
  html, body { width: 1200px; height: 810px; overflow: hidden; }
  body {
    background: var(--backdrop);
    font-family: "Work Sans", sans-serif;
    color: var(--text);
    position: relative;
  }
  .card {
    position: absolute;
    top: 245px;
    width: 560px;
    height: 320px;
    background: var(--card);
    overflow: hidden;
  }
  .card--services { left: 25px; }
  .card--contact { left: 615px; }

  /* Services side */
  .brand-row {
    position: absolute;
    top: 34px;
    left: 0;
    width: 100%;
    display: flex;
    align-items: center;
    justify-content: center;
    gap: 26px;
  }
  .brand-mark {
    width: 70px;
    height: 52px;
    background: var(--purple);
  }
  .brand-name {
    font-family: "Montserrat", sans-serif;
    font-weight: 700;
    letter-spacing: 0.22em;
    text-transform: uppercase;
  }
  .card--services .brand-name { font-size: 40px; color: var(--purple); }
  .services-rule {
    position: absolute;
    left: 0; right: 0;
    top: 130px;
    border-top: 1.5px solid var(--purple);
  }
  .services-divider {
    position: absolute;
    left: 280px;
    top: 130px;
    bottom: 0;
    border-left: 1.5px solid var(--purple);
  }
  .service-col {
    position: absolute;
    top: 130px;
    width: 280px;
    text-align: center;
  }
  .service-col--foam { left: 0; }
  .service-col--enviro { left: 280px; }
  .service-title {
    font-family: "Montserrat", sans-serif;
    font-weight: 700;
    font-size: 17px;
    letter-spacing: 0.2em;
    color: var(--purple);
    padding: 16px 0 10px;
    border-bottom: 1.5px solid var(--purple);
  }
  .service-list {
    list-style: none;
    padding-top: 12px;
    font-size: 12.5px;
    font-weight: 500;
    letter-spacing: 0.06em;
    line-height: 1.3;
    text-transform: uppercase;
  }

  /* Contact side */
  .contact-brand {
    position: absolute;
    top: 34px;
    left: 0;
    width: 100%;
    text-align: center;
  }
  .contact-brand .brand-mark { width: 76px; height: 56px; margin: 0 auto 14px; }
  .card--contact .brand-name { font-size: 30px; color: var(--ink); }
  .contact-divider {
    position: absolute;
    left: 279px;
    top: 150px;
    height: 92px;
    border-left: 1.5px solid var(--ink);
  }
  .contact-col { position: absolute; top: 150px; width: 250px; }
  .contact-col--enviro { right: 297px; text-align: right; }
  .contact-col--foam { left: 298px; }
  .contact-title {
    font-family: "Work Sans", sans-serif;
    font-weight: 500;
    font-size: 17px;
    letter-spacing: 0.04em;
    color: var(--ink);
    margin-bottom: 6px;
  }
  .contact-list { list-style: none; font-size: 12.5px; line-height: 1.6; }
  .contact-list li { display: flex; align-items: center; gap: 8px; }
  .contact-col--enviro .contact-list li { justify-content: flex-end; }
  .contact-icon { width: 11px; height: 11px; flex: none; }
  .address-band {
    position: absolute;
    left: 0; bottom: 0;
    width: 560px; height: 56px;
  }
  .address-text {
    position: absolute;
    left: 140px;
    bottom: 8px;
    width: 350px;
    text-align: center;
    font-size: 11.5px;
    line-height: 16px;
    white-space: nowrap;
    color: #fff;
    letter-spacing: 0.02em;
  }
</style>
</head>
<body>

<section class="card card--services" aria-label="Services side">
  <div class="brand-row">
    <div class="brand-mark"></div>
    <span class="brand-name">Halvorn</span>
  </div>
  <div class="services-rule"></div>
  <div class="services-divider"></div>
  <div class="service-col service-col--foam">
    <h2 class="service-title">SPRAY FROM</h2>
    <ul class="service-list">
      <li>Roofing Foam</li>
      <li>Slabjacking</li>
      <li>2Pound/Half Pound</li>
      <li>Sound Proofing</li>
      <li>Batt Insulation</li>
      <li>Attic Blow In</li>
    </ul>
  </div>
  <div class="service-col service-col--enviro">
    <h2 class="service-title">ENVIRONMENTAL</h2>
    <ul class="service-list">
      <li>Air Monitoring</li>
      <li>Asbestos Testing</li>
      <li>Asbestos Removal</li>
      <li>Building Demolition</li>
      <li>Lead Testing</li>
      <li>Mould Removal</li>
    </ul>
  </div>
</section>

<section class="card card--contact" aria-label="Contact side">
  <div class="contact-brand">
    <div class="brand-mark"></div>
    <span class="brand-name">Halvorn</span>
  </div>
  <div class="contact-divider"></div>

  <div class="contact-col contact-col--enviro">
    <h2 class="contact-title">ENVIRONMENTAL</h2>
    <ul class="contact-list">
      <li>604-555-0142
        <svg class="contact-icon" viewBox="0 0 12 12"><path d="M2.5 1h2l1 3-1.3 1a7 7 0 0 0 2.8 2.8L8 6.5l3 1v2A1.5 1.5 0 0 1 9.5 11 8.5 8.5 0 0 1 1 2.5 1.5 1.5 0 0 1 2.5 1z" fill="var(--purple)"/></svg></li>
      <li>enviro1@halvornmail.ca
        <svg class="contact-icon" viewBox="0 0 12 12"><rect x="1" y="2.5" width="10" height="7" fill="none" stroke="var(--purple)" stroke-width="1.3"/><path d="M1 3l5 3.5L11 3" fill="none" stroke="var(--purple)" stroke-width="1.3"/></svg></li>
      <li>www.halvornsprayfoam.ca
        <svg class="contact-icon" viewBox="0 0 12 12"><circle cx="6" cy="6" r="5" fill="none" stroke="var(--purple)" stroke-width="1.2"/><path d="M1 6h10M6 1c-3 3-3 7 0 10M6 1c3 3 3 7 0 10" fill="none" stroke="var(--purple)" stroke-width="1"/></svg></li>
    </ul>
  </div>

  <div class="contact-col contact-col--foam">
    <h2 class="contact-title">SPRAY FOAM</h2>
    <ul class="contact-list">
      <li><svg class="contact-icon" viewBox="0 0 12 12"><path d="M2.5 1h2l1 3-1.3 1a7 7 0 0 0 2.8 2.8L8 6.5l3 1v2A1.5 1.5 0 0 1 9.5 11 8.5 8.5 0 0 1 1 2.5 1.5 1.5 0 0 1 2.5 1z" fill="var(--purple)"/></svg>604-555-0178</li>
      <li><svg class="contact-icon" viewBox="0 0 12 12"><rect x="1" y="2.5" width="10" height="7" fill="none" stroke="var(--purple)" stroke-width="1.3"/><path d="M1 3l5 3.5L11 3" fill="none" stroke="var(--purple)" stroke-width="1.3"/></svg>halvornfoam@halvornmail.ca</li>
      <li><svg class="contact-icon" viewBox="0 0 12 12"><circle cx="6" cy="6" r="5" fill="none" stroke="var(--purple)" stroke-width="1.2"/><path d="M1 6h10M6 1c-3 3-3 7 0 10M6 1c3 3 3 7 0 10" fill="none" stroke="var(--purple)" stroke-width="1"/></svg>www.halvornsprayfoam.ca</li>
    </ul>
  </div>

  <svg class="address-band" viewBox="0 0 560 56" aria-hidden="true">
    <polygon points="0,36 110,36 132,56 0,56" fill="var(--purple)"/>
    <polygon points="114,26 500,26 500,56 138,56" fill="var(--grey-band)"/>
    <polygon points="507,14 560,14 560,56 507,56" fill="var(--purple)"/>
  </svg>
  <p class="address-text">48 Larchmont Way Burnaby, British Columbia v5x 2k4, CA</p>
</section>

</body>
</html>
```